Business card for exciting VC company

Should look simple, crisp, and modern.

Industry/Entity Type

Venture Capital

Contact Information for Business Card

Would like to see at least one design that has our blue on the back with the tagline "Transforming Traditional Industry" and white front with contact details.

Font styles to use
Sans Serif

Requirements
Must have
• Logo

Gregory Tallis
gtallis@brindlewave.vc
Managing Partner
M (628)354-xxxx

```html
<!DOCTYPE html>
<html lang="en">
<head>
<meta charset="utf-8">
<title>Brindlewave Capital – Business Card</title>
<link rel="stylesheet" href="https://fonts.googleapis.com/css2?family=Montserrat:wght@500;700&family=Open+Sans:wght@400&display=swap">
<style>
  :root {
    --brand-blue: #4282c6;
    --ink: #111111;
    --ink-soft: #333333;
    --paper: #ffffff;
    --stage: #2b2b2b;
  }
  * { box-sizing: border-box; margin: 0; padding: 0; }
  html, body {
    width: 1200px;
    height: 900px;
    overflow: hidden;
    background: var(--stage);
  }
  .stage {
    width: 1200px;
    height: 900px;
    display: flex;
    flex-direction: column;
    align-items: center;
    justify-content: center;
    gap: 40px;
  }
  .card {
    width: 700px;
    height: 400px;
    position: relative;
  }

  /* Front */
  .card-front {
    background: var(--paper);
    display: flex;
    align-items: center;
    padding: 0 56px;
  }
  .wordmark {
    font-family: "Montserrat", sans-serif;
    font-weight: 500;
    color: var(--ink);
    font-size: 30px;
    letter-spacing: 0.06em;
    text-transform: uppercase;
    line-height: 1.2;
    width: 300px;
  }
  .divider {
    width: 1px;
    height: 130px;
    background: var(--brand-blue);
    margin: 0 30px;
  }
  .contact {
    font-family: "Open Sans", sans-serif;
    color: var(--ink-soft);
  }
  .contact-name {
    font-family: "Montserrat", sans-serif;
    font-weight: 700;
    color: var(--brand-blue);
    font-size: 21px;
    letter-spacing: 0.04em;
    text-transform: uppercase;
  }
  .contact-title {
    font-size: 15px;
    margin: 2px 0 18px;
  }
  .contact-line {
    display: flex;
    align-items: center;
    gap: 8px;
    font-size: 14.5px;
    margin-top: 6px;
  }
  .contact-line svg { width: 13px; height: 13px; fill: var(--brand-blue); flex: none; }

  /* Back */
  .card-back {
    background: var(--brand-blue);
    color: var(--paper);
    display: flex;
    flex-direction: column;
    align-items: center;
    justify-content: center;
    gap: 46px;
  }
  .card-back .wordmark {
    color: var(--paper);
    width: auto;
    text-align: center;
    font-size: 40px;
    letter-spacing: 0.08em;
  }
  .tagline {
    font-family: "Open Sans", sans-serif;
    font-size: 14px;
    letter-spacing: 0.06em;
    text-transform: uppercase;
  }
</style>
</head>
<body>
  <main class="stage">
    <section class="card card-front" aria-label="Card front">
      <div class="wordmark">Brindlewave<br>Capital</div>
      <div class="divider"></div>
      <div class="contact">
        <p class="contact-name">Gregory Tallis</p>
        <p class="contact-title">Managing Partner</p>
        <p class="contact-line">
          <svg viewBox="0 0 24 24" aria-hidden="true"><path d="M6.6 10.8a15.1 15.1 0 0 0 6.6 6.6l2.2-2.2a1 1 0 0 1 1-.25 11.4 11.4 0 0 0 3.6.57 1 1 0 0 1 1 1V20a1 1 0 0 1-1 1A17 17 0 0 1 3 4a1 1 0 0 1 1-1h3.5a1 1 0 0 1 1 1c0 1.25.2 2.45.57 3.57a1 1 0 0 1-.25 1z"/></svg>
          (628)354-xxxx
        </p>
        <p class="contact-line">
          <svg viewBox="0 0 24 24" aria-hidden="true"><path d="M2 5h20v14H2z M2 5l10 8 10-8" fill-rule="evenodd"/><path d="M3 6.2v11.8h18V6.2l-9 7.2z"/></svg>
          gtallis@brindlewave.vc
        </p>
      </div>
    </section>

    <section class="card card-back" aria-label="Card back">
      <div class="wordmark">Brindlewave Capital</div>
      <p class="tagline">Transforming Traditional Industry</p>
    </section>
  </main>
</body>
</html>
```